Old Shanghai birthday party (1920s - 1930s)

I need an invitation for a joint birthday party; basically we will celebrate a couple: she's turning 40 and he's turning 45). The idea of the venue decoration is very sophisticate, with red lanterns, old style painted paper umbrellas and fans, check it out for your reference
https://www.tackboardly.com/rennavost/jazz-harbour/
Here the details to write down:
Marta and Dennis
are turning 85 !
Come celebrate with us!
Saturday, September 10th, 2016 at 8 pm
Quillberry
7C, 19 Tai Lok Fung Road, Aberdeen, Hong Kong
If you can come, please RSVP to Marta Felcote by August 20th
at (852) 471 26508
Dress code: Old Shanghai

Target Market(s)
Adults around 40 years old (The couple is from Australia)

```html
<!DOCTYPE html>
<html lang="en">
<head>
<meta charset="utf-8">
<title>Marta and Dennis – Old Shanghai Birthday Invitation</title>
<link rel="stylesheet" href="https://fonts.googleapis.com/css2?family=Great+Vibes&family=Playfair+Display:ital,wght@1,700&family=Mulish:wght@400;700;800&display=swap">
<style>
  :root {
    --paper: #ebebeb;
    --paper-light: #f4f4f4;
    --lacquer: #a3171b;
    --lacquer-deep: #7e1013;
    --ink: #141414;
    --white: #ffffff;
  }
  * { margin: 0; padding: 0; box-sizing: border-box; }
  html, body { width: 848px; height: 1200px; overflow: hidden; background: var(--paper); }
  .invitation {
    position: relative;
    width: 848px;
    height: 1200px;
    overflow: hidden;
    background: radial-gradient(ellipse at center, var(--paper-light) 0%, var(--paper) 70%);
    font-family: "Mulish", "Century Gothic", sans-serif;
    color: var(--lacquer);
  }
  .frame { position: absolute; inset: 0; }
  .lanterns { position: absolute; top: 0; height: 720px; }
  .lanterns--left { left: 0; width: 170px; }
  .lanterns--right { right: 0; width: 170px; }
  .title { position: absolute; inset: 0; font-weight: 400; }
  .names {
    position: absolute;
    left: 0; right: 0;
    font-family: "Great Vibes", "Snell Roundhand", cursive;
    color: var(--lacquer);
    line-height: 1;
    text-align: center;
    white-space: nowrap;
  }
  .names__first { top: 110px; font-size: 178px; padding-right: 10px; }
  .names__second { top: 270px; font-size: 170px; padding-right: 100px; }
  .names__and {
    position: absolute;
    top: 292px; left: 588px;
    font-family: "Playfair Display", Georgia, serif;
    font-style: italic;
    font-weight: 700;
    font-size: 38px;
    line-height: 1;
    color: var(--lacquer);
  }
  .line { position: absolute; left: 0; right: 0; text-align: center; }
  .tagline { top: 446px; font-size: 33px; }
  .tagline--call { top: 516px; font-size: 36px; }
  .rule { position: absolute; left: 176px; width: 498px; height: 2px; background: var(--ink); }
  .rule--top { top: 623px; }
  .rule--bottom { top: 770px; }
  .date {
    top: 650px;
    font-size: 38px;
    font-weight: 800;
    color: var(--ink);
    line-height: 47px;
    text-transform: uppercase;
  }
  .venue { top: 826px; font-size: 27px; }
  .address { top: 896px; font-size: 29px; line-height: 37px; }
  .rsvp { top: 1012px; font-size: 16px; line-height: 21px; }
  .rsvp strong { color: var(--ink); font-weight: 400; }
  .dress-code {
    position: absolute;
    left: 229px; top: 1104px;
    width: 390px; height: 43px;
    background: var(--lacquer);
    color: var(--white);
    font-size: 23px;
    font-weight: 700;
    display: flex; align-items: center; justify-content: center;
    text-transform: uppercase;
  }
</style>
</head>
<body>
<main class="invitation">
  <svg class="frame" width="848" height="1200" viewBox="0 0 848 1200" aria-hidden="true">
    <g fill="none" stroke="var(--lacquer)" stroke-width="4">
      <path d="M110 16 H738 V44 H795 V100 H768 V1100 H795 V1173 H738 V1146 H110 V1173 H56 V1100 H84 V100 H56 V44 H110 Z"/>
      <rect x="84" y="44" width="684" height="1102"/>
      <rect x="106" y="66" width="640" height="1058" stroke-width="3"/>
      <rect x="56" y="16" width="54" height="28"/>
      <rect x="738" y="16" width="57" height="28"/>
      <rect x="56" y="1146" width="54" height="27"/>
      <rect x="738" y="1146" width="57" height="27"/>
    </g>
  </svg>

  <svg class="lanterns lanterns--left" viewBox="0 0 170 720" preserveAspectRatio="none" role="img" aria-label="Column of hanging red paper lanterns with gold tassels">
    <defs>
      <linearGradient id="lanternFadeLeft" x1="0" y1="0" x2="0" y2="1">
        <stop offset="0" stop-color="var(--lacquer)"/>
        <stop offset="0.5" stop-color="var(--lacquer-deep)" stop-opacity="0.8"/>
        <stop offset="1" stop-color="var(--lacquer)" stop-opacity="0"/>
      </linearGradient>
    </defs>
    <rect width="170" height="720" fill="url(#lanternFadeLeft)"/>
  </svg>
  <svg class="lanterns lanterns--right" viewBox="0 0 170 720" preserveAspectRatio="none" role="img" aria-label="Column of hanging red paper lanterns with gold tassels">
    <defs>
      <linearGradient id="lanternFadeRight" x1="0" y1="0" x2="0" y2="1">
        <stop offset="0" stop-color="var(--lacquer)"/>
        <stop offset="0.5" stop-color="var(--lacquer-deep)" stop-opacity="0.8"/>
        <stop offset="1" stop-color="var(--lacquer)" stop-opacity="0"/>
      </linearGradient>
    </defs>
    <rect width="170" height="720" fill="url(#lanternFadeRight)"/>
  </svg>

  <h1 class="title">
    <span class="names names__first">Marta</span>
    <span class="names__and">and</span>
    <span class="names names__second">Dennis</span>
  </h1>

  <p class="line tagline">are turning 85 !</p>
  <p class="line tagline tagline--call">Come celebrate with us!</p>

  <div class="rule rule--top"></div>
  <p class="line date">Saturday, September<br>10th, 2016 at 8 pm</p>
  <div class="rule rule--bottom"></div>

  <p class="line venue">Quillberry</p>
  <p class="line address">7C, 19 Tai Lok Fung Road,<br>Aberdeen, Hong Kong</p>

  <p class="line rsvp">If you can come, please RSVP to <strong>Marta Felcote</strong> by August 20th<br><strong>at (852) 471 26508</strong></p>

  <div class="dress-code">Dress code: Old Shanghai</div>
</main>
</body>
</html>
```